Wine Label for a Sweet Wine Called "Glimmo"

We need a wine label that will be used for both a sweet red and a sweet white wine. The very important thing to remember is the target market for these wines is: young American women who love sweet wines and they also spend a lot of their money on their hair, clothes, jewelry, nails. They LOVE Glimmo (Glimmo is a word used to describe flashy accessories, jewelry, decoration.) This label needs to be eye catching, showy, fun, glittery. Please put the brand name, "Glimmo," big, and then in smaller but still readable words underneath the label or somewhere on the label: Sweet, Sophisticated, Red (or white). (An example of what I mean is attached). To differentiate between the two color wines you can suggest color changes to differentiate between the red label and the white label but the label design itself should be the same. Ultimately, the label can be the exact same label for both white and red as long as it looks good on a white wine (a greenish/yellow wine in a clear glass bottle) and a red wine (a dark color wine in a dark bottle).

I've attached an example of the text size relationship between the word Glimmo and the words to go underneath or elsewhere on the label, but you can certainly play with this-- it is just a suggestion of the text size relationship, and definitely NOT at all mandatory that you use any of these fonts.

You can pick the size of the label but try to stay within normal wine label sizes, meaning don't go bigger than approx. 3.5 inches wide and 5 inches tall.

Target Market(s)

Young American women who love sweet wines and spend a lot of money on their hair, clothes, jewelry, nails. They love Glimmo (Glimmo is a word that means flashy accessories, jewelry, decoration)

Requirements
Must have
• It needs to be flashy, glittery, fun, eye catching, memorable
Nice to have
• It shouldn't be too too ultra feminine! The target market is strong independent women and we also have men who will buy it too.

```html
<!DOCTYPE html>
<html lang="en">
<head>
<meta charset="utf-8">
<title>Glimmo Wine Label</title>
<link rel="stylesheet" href="https://fonts.googleapis.com/css2?family=Cinzel:wght@400;500;600&family=Cormorant+Garamond:wght@500;600&family=Lato:wght@400;700&display=swap">
<style>
  :root {
    --backdrop: #141414;
    --label: #2d2239;
    --label-edge: #221a2c;
    --gold: #d4ad5e;
    --gold-light: #f0d892;
    --gold-deep: #9a7a3c;
    --sparkle: #fff3c9;
    --ink-light: #e2d8c8;
    --ink-soft: #b0a392;
  }
  * { margin: 0; padding: 0; box-sizing: border-box; }
  html, body {
    width: 1200px; height: 1200px; overflow: hidden;
    background: var(--backdrop);
  }
  .canvas {
    width: 1200px; height: 1200px;
    display: flex; align-items: center; justify-content: center;
  }
  .label {
    position: relative;
    width: 600px; height: 980px;
    background:
      radial-gradient(circle at 12% 18%, rgba(255,236,170,0.35) 0 1.2px, transparent 2px),
      radial-gradient(circle at 63% 41%, rgba(255,236,170,0.28) 0 1px, transparent 1.8px),
      radial-gradient(circle at 37% 77%, rgba(255,236,170,0.3) 0 1.1px, transparent 1.9px),
      radial-gradient(circle at 86% 64%, rgba(255,236,170,0.25) 0 0.9px, transparent 1.6px),
      linear-gradient(180deg, var(--label) 0%, var(--label-edge) 100%);
    background-size: 46px 46px, 38px 38px, 54px 54px, 31px 31px, 100% 100%;
    text-align: center;
    color: var(--ink-light);
  }
  .frame { position: absolute; inset: 0; }
  .crest {
    position: absolute; left: 210px; top: 92px;
    width: 180px; height: 120px;
    border-radius: 50%;
    background: radial-gradient(ellipse at center, rgba(240,216,146,0.6) 0%, rgba(212,173,94,0.2) 55%, rgba(212,173,94,0) 75%);
  }
  .brand {
    position: absolute; left: 0; right: 0; top: 222px;
    font-family: "Cinzel", serif;
    font-weight: 600;
    font-size: 64px; line-height: 80px;
    letter-spacing: 6px;
    color: var(--gold-light);
    display: flex; align-items: center; justify-content: center; gap: 24px;
  }
  .brand-dash { display: inline-block; width: 26px; height: 2px; background: var(--gold); }
  .tagline {
    position: absolute; left: 0; right: 0; top: 314px;
    font-family: "Cinzel", serif;
    font-weight: 500;
    font-size: 19px; letter-spacing: 4px;
    color: var(--gold);
  }
  .tagline .dot { padding: 0 8px; color: var(--sparkle); }
  .flourish {
    position: absolute; left: 170px; top: 356px;
    width: 260px; height: 92px;
    border-radius: 50%;
    background: radial-gradient(ellipse at 50% 35%, rgba(240,216,146,0.55) 0%, rgba(212,173,94,0.17) 55%, rgba(212,173,94,0) 75%);
  }
  .varietal {
    position: absolute; left: 0; right: 0; top: 518px;
    font-family: "Cormorant Garamond", serif;
    font-weight: 600;
    font-size: 27px; letter-spacing: 1.5px;
    color: var(--ink-light);
  }
  .year-caption {
    position: absolute; left: 0; right: 0; top: 572px;
    display: flex; align-items: center; justify-content: center; gap: 26px;
    font-family: "Lato", sans-serif;
    font-size: 11px; letter-spacing: 1.5px;
    color: var(--ink-soft);
  }
  .year-caption .rule { width: 36px; height: 1px; background: var(--ink-soft); }
  .vintage {
    position: absolute; left: 0; right: 0; top: 606px;
    font-family: "Cormorant Garamond", serif;
    font-weight: 600;
    font-size: 44px; letter-spacing: 2px;
    font-variant-numeric: lining-nums;
    color: var(--ink-light);
  }
  .origin-band {
    position: absolute; left: 80px; top: 690px;
    width: 440px; height: 28px;
    background: linear-gradient(90deg, var(--gold-deep) 0%, var(--gold-light) 30%, var(--sparkle) 45%, var(--gold) 70%, var(--gold-deep) 100%);
    font-family: "Cormorant Garamond", serif;
    font-weight: 600;
    font-size: 17px; letter-spacing: 1px; line-height: 28px;
    color: var(--label);
  }
  .volume {
    position: absolute; left: 0; right: 0; top: 744px;
    font-family: "Lato", sans-serif;
    font-size: 11px; letter-spacing: 1.5px;
    color: var(--ink-soft);
  }
  .bottler {
    position: absolute; left: 0; right: 0; top: 784px;
    font-family: "Lato", sans-serif;
    font-size: 10px; line-height: 17px;
    color: var(--ink-soft);
  }
</style>
</head>
<body>
<main class="canvas">
  <section class="label">
    <svg class="frame" width="600" height="980" viewBox="0 0 600 980" aria-hidden="true">
      <defs>
        <linearGradient id="goldLine" x1="0" y1="0" x2="1" y2="0">
          <stop offset="0" stop-color="#9a7a3c"/>
          <stop offset="0.5" stop-color="#f0d892"/>
          <stop offset="1" stop-color="#9a7a3c"/>
        </linearGradient>
      </defs>
      <g stroke="url(#goldLine)" fill="none">
        <rect x="30" y="30" width="540" height="920" stroke-width="1.5"/>
        <rect x="38" y="38" width="524" height="904" stroke-width="0.6"/>
      </g>
      <g fill="var(--gold-light)">
        <path d="M300 18 L308 30 L300 42 L292 30 Z"/>
        <path d="M300 938 L308 950 L300 962 L292 950 Z"/>
        <path d="M30 480 L36 490 L30 500 L24 490 Z"/>
        <path d="M570 480 L576 490 L570 500 L564 490 Z"/>
        <path d="M300 462 L304 472 L300 482 L296 472 Z"/>
      </g>
      <g fill="var(--sparkle)">
        <path d="M112 250 Q114 260 124 262 Q114 264 112 274 Q110 264 100 262 Q110 260 112 250 Z"/>
        <path d="M488 226 Q490 234 498 236 Q490 238 488 246 Q486 238 478 236 Q486 234 488 226 Z"/>
        <path d="M470 300 Q471 305 476 306 Q471 307 470 312 Q469 307 464 306 Q469 305 470 300 Z"/>
        <path d="M134 318 Q135 323 140 324 Q135 325 134 330 Q133 325 128 324 Q133 323 134 318 Z"/>
        <path d="M520 694 Q522 702 530 704 Q522 706 520 714 Q518 706 510 704 Q518 702 520 694 Z"/>
      </g>
    </svg>

    <div class="crest" role="img" aria-label="Gold ornamental scrollwork crest"></div>

    <h1 class="brand"><span class="brand-dash"></span>GLIMMO<span class="brand-dash"></span></h1>
    <p class="tagline">SWEET<span class="dot">•</span>SOPHISTICATED<span class="dot">•</span>RED</p>

    <div class="flourish" role="img" aria-label="Gold ornamental scrollwork flourish"></div>

    <p class="varietal">CABERNET SAVINGDNON</p>
    <p class="year-caption"><span class="rule"></span>YEAR<span class="rule"></span></p>
    <p class="vintage">2016</p>
    <p class="origin-band">PRODUCT OF USA</p>
    <p class="volume">ALC. 13.5% BY VOL • 750 ML</p>
    <p class="bottler">Fermented &amp; bottled by:<br>Company name, LTD<br>Street 12346, Place,<br>USA<br>Contains Sulfites</p>
  </section>
</main>
</body>
</html>
```